Dental Lab Delivery Box Design 163x115x97mm

* AI file of the box attached
* Full-Color outside and one color inside
* Return pictures of the 3D design; so we can have a better idea of how it will turn out
* Match Logo Color and Design
* Please find attached Words doc for the wording
* Research the dental lab delivery
* Attached our sister lab dental lab design
*
Updates

Target Market(s)

Dental Office

Industry/Entity Type

Dental Lab

Font styles to use
Serif

Colors
0054AA
0677BA
7BADD7
CADEEF
E8F1F8

Requirements
Must have
• Advance, Clean, and Matched Logo color
Nice to have
• Graphics
Should not have
• Too much words or over advertise

```html
<!DOCTYPE html>
<html lang="en">
<head>
<meta charset="utf-8">
<title>Veldo Dental Inc – Delivery Box Dieline</title>
<link rel="stylesheet" href="https://fonts.googleapis.com/css2?family=Montserrat:wght@400;500;600;700&display=swap">
<style>
  :root {
    --stage: #afafaf;
    --cut: #e0177f;
    --score: #2b2b2b;
    --navy-deep: #0a1f5c;
    --navy: #0f3d8c;
    --blue-brand: #1e4f9c;
    --blue-mid: #0677ba;
    --blue-light: #5aaee0;
    --mist: #e8ecf3;
    --paper: #ffffff;
    --ink: #333333;
    --text-grey: #555555;
  }
  html, body {
    margin: 0;
    padding: 0;
    width: 1200px;
    height: 1126px;
    overflow: hidden;
    background: var(--stage);
  }
  .dieline {
    display: block;
    width: 1200px;
    height: 1126px;
    font-family: "Montserrat", sans-serif;
  }
  .cut { stroke: var(--cut); stroke-width: 1; }
  .score { stroke: var(--score); stroke-width: 1; }
  .panel-white { fill: url(#paperSheen); }
  .panel-blue { fill: url(#navyField); }
  .brand-name { font-weight: 600; letter-spacing: 1px; }
  .brand-on-blue { fill: var(--paper); }
  .brand-on-white { fill: var(--blue-brand); }
  .info-heading { fill: var(--blue-brand); font-weight: 700; font-size: 10px; }
  .info-body { fill: var(--text-grey); font-size: 8.6px; }
  .signature-title { fill: var(--blue-brand); font-weight: 700; font-size: 11.5px; }
  .signature-line { fill: var(--text-grey); font-weight: 500; font-size: 11px; }
  .legend-label { fill: var(--ink); font-size: 13.5px; }
  .legend-size { fill: var(--ink); font-size: 13.5px; letter-spacing: 0.3px; }
  .soft-arc { fill: var(--mist); opacity: 0.7; }
  .brand-dot { fill: none; stroke: var(--blue-light); stroke-width: 6; opacity: 0.55; }
</style>
</head>
<body>
<svg class="dieline" viewBox="0 0 1200 1126" xmlns="http://www.w3.org/2000/svg">
  <defs>
    <linearGradient id="navyField" x1="0" y1="0" x2="1" y2="1">
      <stop offset="0" stop-color="#081a55"/>
      <stop offset="0.45" stop-color="#0d3a8a"/>
      <stop offset="1" stop-color="#1a55a3"/>
    </linearGradient>
    <linearGradient id="paperSheen" x1="0" y1="0" x2="1" y2="1">
      <stop offset="0" stop-color="#ffffff"/>
      <stop offset="0.55" stop-color="#f7f8fb"/>
      <stop offset="1" stop-color="#e6eaf1"/>
    </linearGradient>
  </defs>

  <!-- Top lid -->
  <g class="lid-top">
    <path class="panel-white cut" d="M330,37 H437 V224 H368 L330,205 Z"/>
    <path class="panel-white cut" d="M775,37 H882 V205 L843,224 H775 Z"/>
    <rect class="panel-blue" x="437" y="37" width="338" height="191"/>
    <g transform="rotate(180 606 130)">
      <text class="brand-name brand-on-blue" x="606" y="135" text-anchor="middle" font-size="38">VELDO</text>
      <text class="brand-name brand-on-blue" x="606" y="158" text-anchor="middle" font-size="12" letter-spacing="5">DENTAL INC</text>
    </g>
  </g>

  <!-- Middle row -->
  <g class="middle-row">
    <path class="panel-white cut" d="M37,234 H227 V455 H37 V395 L29,392 V300 L37,297 Z"/>
    <path class="panel-white cut" d="M227,234 L237,228 V461 L227,455 Z"/>
    <rect class="panel-white" x="237" y="228" width="195" height="233"/>
    <path class="soft-arc" d="M300,461 Q360,330 432,300 V461 Z"/>
    <circle class="brand-dot" cx="334" cy="340" r="44"/>
    <line class="cut" x1="237" y1="228" x2="432" y2="228"/>
    <line class="cut" x1="237" y1="461" x2="432" y2="461"/>
    <line class="score" x1="237" y1="228" x2="237" y2="461"/>

    <rect class="panel-white" x="432" y="228" width="348" height="233"/>
    <path class="soft-arc" d="M500,461 Q600,330 780,310 V461 Z"/>
    <rect class="score" x="432" y="228" width="348" height="233" fill="none"/>
    <rect x="432" y="296" width="9" height="96" rx="4" fill="var(--paper)" class="cut"/>
    <rect x="771" y="296" width="9" height="96" rx="4" fill="var(--paper)" class="cut"/>
    <g transform="rotate(180 606 345)">
      <circle cx="606" cy="243" r="7" fill="none" stroke="var(--blue-mid)" stroke-width="2"/>
      <text class="info-heading" x="606" y="275" text-anchor="middle">COMPANY INFORMATION</text>
      <text class="info-body" x="606" y="298" text-anchor="middle">Welcome to Veldo! Headquartered in Riverton, Oregon,</text>
      <text class="info-body" x="606" y="309" text-anchor="middle">we are a Full digital dental lab for all you</text>
      <text class="info-body" x="606" y="320" text-anchor="middle">need. We strive to build excellent relationship and</text>
      <text class="info-body" x="606" y="331" text-anchor="middle">services with our clients, utilize highly experienced</text>
      <text class="info-body" x="606" y="342" text-anchor="middle">technicians and advance case management systems.</text>
      <text class="info-body" x="606" y="353" text-anchor="middle">Veldo stands for Vision, Excellence, Lab, Detail, Outcome.</text>
      <text class="info-body" x="606" y="364" text-anchor="middle">We care for your team as one team.</text>
      <text class="info-body" x="606" y="385" text-anchor="middle">Veldo looks forward to building and improve your</text>
      <text class="info-body" x="606" y="396" text-anchor="middle">reputation and bringing more smiles to our services.</text>
    </g>

    <rect class="panel-white" x="780" y="228" width="195" height="233"/>
    <circle class="brand-dot" cx="876" cy="345" r="44"/>
    <line class="cut" x1="780" y1="228" x2="975" y2="228"/>
    <line class="cut" x1="780" y1="461" x2="975" y2="461"/>
    <line class="score" x1="975" y1="228" x2="975" y2="461"/>
    <path class="panel-white cut" d="M975,228 L985,234 V455 L975,461 Z"/>
    <path class="panel-white cut" d="M985,234 H1175 V297 L1183,300 V392 L1175,395 V455 H985 Z"/>
  </g>

  <!-- Back panel -->
  <g class="back-panel">
    <path class="panel-white cut" d="M330,484 L367,465 H436 V652 H330 Z"/>
    <path class="panel-white cut" d="M776,465 H845 L883,484 V652 H776 Z"/>
    <path class="soft-arc" d="M800,465 Q850,500 883,520 V652 H850 Q820,560 800,465 Z"/>
    <rect class="panel-blue" x="436" y="461" width="340" height="194"/>
    <g transform="rotate(180 606 555)">
      <text class="brand-name brand-on-blue" x="606" y="560" text-anchor="middle" font-size="38">VELDO</text>
      <text class="brand-name brand-on-blue" x="606" y="583" text-anchor="middle" font-size="12" letter-spacing="5">DENTAL INC</text>
    </g>
  </g>

  <!-- Front panel -->
  <g class="front-panel">
    <path class="panel-white cut" d="M443,656 L300,694 Q249,708 249,745 V805 Q249,840 300,853 L443,893 Z"/>
    <path class="panel-white cut" d="M769,656 L912,694 Q963,708 963,745 V805 Q963,840 912,853 L769,893 Z"/>
    <rect class="panel-white" x="443" y="656" width="326" height="237"/>
    <path class="soft-arc" d="M560,893 Q660,770 769,760 V893 Z"/>
    <rect class="score" x="443" y="656" width="326" height="237" fill="none"/>
    <circle cx="520" cy="760" r="62" fill="none" stroke="var(--blue-brand)" stroke-width="10" opacity="0.85"/>
    <text class="brand-name brand-on-white" x="739" y="752" text-anchor="end" font-size="31">VELDO</text>
    <text class="brand-name brand-on-white" x="739" y="768" text-anchor="end" font-size="10" letter-spacing="4">DENTAL INC</text>
    <text class="signature-title" x="678" y="828" text-anchor="middle">SIGNATURE WORD</text>
    <text class="signature-line" x="678" y="841" text-anchor="middle">Lab with Confidence</text>
    <text class="signature-line" x="678" y="854" text-anchor="middle">Every detail Matters</text>
  </g>

  <!-- Bottom tuck -->
  <g class="bottom-tuck">
    <path class="panel-white cut" d="M435,905 H300 Q252,905 252,950 Q258,1040 330,1075 Q370,1088 435,1088 Z"/>
    <path class="panel-white cut" d="M777,905 H912 Q960,905 960,950 Q954,1040 882,1075 Q842,1088 777,1088 Z"/>
    <path class="panel-blue" d="M443,893 H769 L777,905 V1088 H435 V905 Z"/>
    <text class="brand-name brand-on-blue" x="606" y="1002" text-anchor="middle" font-size="38">VELDO</text>
    <text class="brand-name brand-on-blue" x="612" y="1019" text-anchor="middle" font-size="12" letter-spacing="5">DENTAL INC</text>
  </g>

  <!-- Legend -->
  <g class="legend">
    <text class="legend-label" x="105" y="1018" text-anchor="middle">Cut Line</text>
    <line class="cut" x1="51" y1="1026" x2="158" y2="1026"/>
    <text class="legend-label" x="105" y="1050" text-anchor="middle">Score Line</text>
    <line class="score" x1="51" y1="1057" x2="158" y2="1057"/>
    <text class="legend-size" x="15" y="1097">Inner size:163x115x97mm</text>
  </g>
</svg>
</body>
</html>
```